Author/ Speaker Business Card design

I need a business card designed that will go with the branding that is already on my book and website. I like clean and straightforward, but I am not opposed to something more 'innovative'.

Target Market(s)

Colleges and Universities, educational institutions

Industry/Entity Type

Education

Contact Information for Business Card

Standard size. It should be able to be printed on good quality white or ivory paper.

Font styles to use
Sans Serif

Colors
0355a3

Requirements
Must have
• There's a blue on my website. It should have some blue. My logo is at the top. It should have the logo incorporated somewhere on it. My name, Author | Speaker | Teacher | Trainer, my phone number (+31 64-207 5819), my email address (milo@theboldlearner.example), Social media icons (twitter, Instagram, LinkedIn) with the addresses (twitter @writermilofenwick, Instagram - theboldlearner, LinkedIn - theboldlearner) By they way, the website is www.theboldlearner.example. There is a photo of the book on the website. Also, my full name is Milo Fenwick
Nice to have
• Try to use the font that is on the website and book. Also, if you could get that blue, that would be great.
Should not have
• My photo

```html
<!DOCTYPE html>
<html lang="en">
<head>
<meta charset="utf-8">
<title>The Bold Learner – Business Card</title>
<link rel="stylesheet" href="https://fonts.googleapis.com/css2?family=Mulish:wght@400;600;800&family=Didact+Gothic&display=swap">
<style>
  :root {
    --brand-blue: #0355a3;
    --band-blue: #0657a8;
    --band-edge: #5b93cf;
    --paper: #ffffff;
    --ink: #1d1d1f;
    --backdrop: #e6e7ea;
  }
  * { box-sizing: border-box; margin: 0; padding: 0; }
  html, body {
    width: 1200px; height: 1000px; overflow: hidden;
    background: var(--backdrop);
  }
  .business-card {
    position: absolute; left: 100px; top: 214px;
    width: 1000px; height: 572px;
    background: var(--paper);
    border-radius: 40px;
    overflow: hidden;
    box-shadow: 0 10px 30px rgba(0,0,0,.18);
    font-family: "Didact Gothic", "Century Gothic", sans-serif;
  }
  .brand {
    position: absolute; left: 0; right: 0; top: 62px;
    display: flex; justify-content: center; align-items: center; gap: 22px;
  }
  .brand-dot {
    width: 58px; height: 58px; border-radius: 50%;
    background: var(--brand-blue);
  }
  .brand-name {
    font-family: "Mulish", sans-serif; font-weight: 800;
    font-size: 64px; line-height: 1; color: var(--brand-blue);
    letter-spacing: -0.5px;
  }
  .holder {
    position: absolute; left: 0; right: 0; top: 232px; text-align: center;
  }
  .holder-name {
    font-family: "Mulish", sans-serif; font-weight: 800;
    font-size: 42px; color: var(--brand-blue); line-height: 1.1;
  }
  .holder-roles {
    font-size: 22px; color: var(--ink); margin-top: 6px; letter-spacing: .3px;
  }
  .contact-band {
    position: absolute; left: 0; right: 0; bottom: 0; height: 210px;
    background: var(--band-blue);
    border-top: 6px solid var(--band-edge);
    color: #fff;
    display: flex; justify-content: center; gap: 70px;
    padding-top: 34px;
    font-size: 24px;
  }
  .contact-column { display: flex; flex-direction: column; gap: 14px; }
  .contact-column.primary { align-items: flex-end; }
  .contact-column.secondary { padding-top: 48px; }
  .contact-item { display: flex; align-items: center; gap: 10px; white-space: nowrap; }
  .contact-item svg { width: 22px; height: 22px; flex: none; }
  .social-mark { width: 18px; height: 18px; border-radius: 50%; background: #fff; flex: none; }
  .web strong { font-family: "Mulish", sans-serif; font-weight: 800; }
</style>
</head>
<body>
  <div class="business-card">
    <div class="brand">
      <span class="brand-dot"></span>
      <span class="brand-name">The Bold Learner</span>
    </div>

    <div class="holder">
      <h1 class="holder-name">Milo Fenwick</h1>
      <p class="holder-roles">Author | Speaker | Teacher | Trainer</p>
    </div>

    <div class="contact-band">
      <div class="contact-column primary">
        <div class="contact-item">
          <svg viewBox="0 0 24 24" aria-hidden="true"><path fill="#fff" d="M6.6 10.8a15.5 15.5 0 0 0 6.6 6.6l2.2-2.2c.3-.3.7-.4 1-.2 1.1.4 2.3.6 3.6.6.6 0 1 .4 1 1V20c0 .6-.4 1-1 1A17 17 0 0 1 3 4c0-.6.4-1 1-1h3.5c.6 0 1 .4 1 1 0 1.3.2 2.5.6 3.6.1.3 0 .7-.2 1z"/></svg>
          <span>+31 64-207 5819</span>
        </div>
        <div class="contact-item">
          <svg viewBox="0 0 24 24" aria-hidden="true"><rect x="2" y="5" width="20" height="14" rx="2" fill="#fff"/><path d="M3 6l9 7 9-7" fill="none" stroke="#0657a8" stroke-width="1.8"/></svg>
          <span>milo@theboldlearner.example</span>
        </div>
        <div class="contact-item">
          <span class="social-mark"></span>
          <span>@writermilofenwick</span>
        </div>
      </div>
      <div class="contact-column secondary">
        <div class="contact-item">
          <span class="social-mark"></span>
          <span>theboldlearner</span>
        </div>
        <div class="contact-item web">
          <svg viewBox="0 0 24 24" aria-hidden="true"><g fill="none" stroke="#fff" stroke-width="1.8"><circle cx="12" cy="12" r="9.5"/><ellipse cx="12" cy="12" rx="4" ry="9.5"/><path d="M2.5 12h19M4 7h16M4 17h16"/></g></svg>
          <span>www.<strong>theboldlearner</strong>.example</span>
        </div>
      </div>
    </div>
  </div>
</body>
</html>
```